Business Card and Letterhead for new HR Consultancy

A business card and letterhead design that includes the logo (attached in jpg) and the business tag line which is "Building Strength in Your People"
We are based in regional New South Wales, Australia and provide HR services to small and medium business owners to support them grow their businesses by focusing on their people. The services provided cover the full range of HR management from simple advice through to comprehensive programs that support people management. My clients typically will not have a HR manager, either because they don't need to employ one or can't afford to hire one. So they will be looking for me to provide good services, add value to their business for a competitive price.
I am a middle aged woman with over 15 years expertise in all facets of HR Management. My clients need to know they can trust me, that I am credible and competent and open in my relationship with them and that I can make a positive difference for them.
I would like to see designs that are modern and communicate value for money.
Updates
A note to advise that the email address is
xxxxxxx@willowbankstaff.com.au
website will be
www.willowbankstaff.com.au
thanks
M.
Will also need to include the business number (indicates it is a registered business).
ABN: 37 218 405 963
Target Market(s)
small to medium sized business owners 30 years and over, professional and tradespeople
Industry/Entity Type
Business
Look and feel

```html
<!DOCTYPE html>
<html lang="en">
<head>
<meta charset="utf-8">
<title>Willowbank Business Cards</title>
<link rel="stylesheet" href="https://fonts.googleapis.com/css2?family=Open+Sans:wght@400;600;700&family=Arimo:wght@400;700&display=swap">
<style>
  :root {
    --green: #0a9246;
    --brown: #7a523d;
    --ink: #1c1c1c;
    --paper: #ffffff;
    --stage: #cfcfcf;
    --rule: #c4c4c4;
  }
  * { box-sizing: border-box; margin: 0; padding: 0; }
  html, body { width: 1200px; height: 724px; overflow: hidden; background: var(--stage); }
  .sheet { position: relative; width: 1200px; height: 724px; }
  .card {
    position: absolute; width: 525px; height: 300px; overflow: hidden;
    box-shadow: 0 1px 3px rgba(0,0,0,.25);
  }
  .card--front-contact { left: 42px; top: 38px; background: var(--paper); }
  .card--front-tagline { left: 42px; top: 378px; background: var(--paper); }
  .card--back-green { left: 619px; top: 38px; background: var(--green); }
  .card--back-brown { left: 619px; top: 378px; background: var(--brown); }

  .brand { position: absolute; display: flex; align-items: center; gap: 14px; }
  .brand__dot { width: 40px; height: 40px; border-radius: 50%; background: var(--green); flex: none; }
  .brand__name { font-family: "Open Sans", sans-serif; font-weight: 600; font-size: 50px; color: var(--green); line-height: 1; letter-spacing: -0.5px; }
  .card--front-contact .brand { left: 74px; top: 46px; }
  .card--front-tagline .brand { left: 74px; top: 84px; }

  .person { position: absolute; right: 276px; top: 166px; text-align: right; font-family: "Arimo", sans-serif; }
  .person__name { font-family: "Open Sans", sans-serif; font-weight: 700; font-size: 17px; color: var(--brown); line-height: 1.1; }
  .person__title { font-size: 14px; color: var(--green); line-height: 1.3; margin-bottom: 6px; }
  .person__address { font-size: 13px; color: var(--ink); line-height: 1.4; }
  .divider { position: absolute; left: 261px; top: 163px; width: 1px; height: 88px; background: var(--rule); }
  .contact { position: absolute; left: 270px; top: 170px; list-style: none; font-family: "Arimo", sans-serif; font-size: 13px; color: var(--ink); }
  .contact li { display: flex; align-items: center; gap: 6px; height: 19.5px; }
  .contact svg { width: 12px; height: 12px; flex: none; }

  .stripe { position: absolute; left: 0; bottom: 0; width: 100%; height: 11px; }

  .tagline-front { position: absolute; left: 0; width: 100%; top: 166px; text-align: center; font-family: "Open Sans", sans-serif; font-weight: 700; font-size: 22px; color: var(--brown); letter-spacing: .3px; }
  .url-front { position: absolute; left: 0; width: 100%; top: 247px; text-align: center; font-family: "Open Sans", sans-serif; font-weight: 700; font-size: 19px; letter-spacing: 2px; color: var(--ink); }
  .url-front__name { color: var(--green); }

  .back__brand { position: absolute; left: 0; width: 100%; top: 48px; display: flex; flex-direction: column; align-items: center; gap: 12px; }
  .back__dot { width: 96px; height: 96px; border-radius: 50%; background: var(--paper); }
  .back__name { font-family: "Open Sans", sans-serif; font-weight: 600; font-size: 30px; color: var(--paper); line-height: 1; }
  .back__tagline { position: absolute; left: 0; width: 100%; top: 222px; text-align: center; font-family: "Open Sans", sans-serif; font-weight: 700; font-size: 16px; color: var(--paper); letter-spacing: .4px; }
  .back__url { position: absolute; left: 0; width: 100%; top: 256px; text-align: center; font-family: "Open Sans", sans-serif; font-size: 22px; color: var(--paper); letter-spacing: .5px; }
</style>
</head>
<body>
<main class="sheet">

  <section class="card card--front-contact">
    <div class="brand"><span class="brand__dot"></span><span class="brand__name">Willowbank</span></div>
    <div class="person">
      <p class="person__name">Your Name</p>
      <p class="person__title">Title</p>
      <p class="person__address">00 Floor Complex Street<br>City Name 000 111</p>
    </div>
    <span class="divider"></span>
    <ul class="contact">
      <li><svg viewBox="0 0 12 12"><circle cx="6" cy="6" r="5.3" fill="none" stroke="#0a9246" stroke-width="1.2"/><path d="M4 3.3l1 .2.4 1.3-.6.6a4 4 0 0 0 1.8 1.8l.6-.6 1.3.4.2 1-.9.8C5.6 8.6 3.4 6.4 3.2 4.2z" fill="#0a9246"/></svg>123-456-7890</li>
      <li><svg viewBox="0 0 12 12"><path d="M2 7l1-3.2h6L10 7v2.5H2z" fill="#0a9246"/><circle cx="3.8" cy="9.6" r="1.1" fill="#0a9246"/><circle cx="8.2" cy="9.6" r="1.1" fill="#0a9246"/></svg>123-456-7890</li>
      <li><svg viewBox="0 0 12 12"><circle cx="6" cy="6" r="5.6" fill="#0a9246"/><rect x="3" y="4" width="6" height="4" fill="#fff"/><path d="M3 4l3 2.2L9 4" fill="none" stroke="#0a9246" stroke-width=".8"/></svg>info@willowbankstaff.com.au</li>
      <li><svg viewBox="0 0 12 12"><circle cx="6" cy="6" r="5.3" fill="none" stroke="#0a9246" stroke-width="1.1"/><ellipse cx="6" cy="6" rx="2.2" ry="5.3" fill="none" stroke="#0a9246" stroke-width=".9"/><path d="M.8 6h10.4" stroke="#0a9246" stroke-width=".9"/></svg>www.willowbankstaff.com.au</li>
    </ul>
    <svg class="stripe" viewBox="0 0 525 11" preserveAspectRatio="none">
      <polygon points="0,0 265,0 254,11 0,11" fill="#0a9246"/>
      <polygon points="273,0 525,0 525,11 262,11" fill="#7a523d"/>
    </svg>
  </section>

  <section class="card card--back-green">
    <div class="back__brand"><span class="back__dot"></span><span class="back__name">Willowbank</span></div>
    <p class="back__tagline">BUILDING STRENGTH IN YOUR PEOPLE</p>
    <p class="back__url">www.willowbankstaff.com.au</p>
  </section>

  <section class="card card--front-tagline">
    <div class="brand"><span class="brand__dot"></span><span class="brand__name">Willowbank</span></div>
    <p class="tagline-front">Building Strength in Your People</p>
    <p class="url-front">www.<span class="url-front__name">willowbankstaff</span>.com.au</p>
  </section>

  <section class="card card--back-brown">
    <div class="back__brand"><span class="back__dot"></span><span class="back__name">Willowbank</span></div>
    <p class="back__tagline">BUILDING STRENGTH IN YOUR PEOPLE</p>
    <p class="back__url">www.willowbankstaff.com.au</p>
  </section>

</main>
</body>
</html>
```